Business Card with PUNCH
bluepinelodge.net
Project: Business Card with PUNCH
Business Card with PUNCH - Consulting
Creative Brief
Simple
Morris Trulsow
President
418 Dunmere Lane Suite 207 Spring, TX 77291
morris@bluepinelodge.net
logo on the back please
mtrulsow mtrulsow
WOW, what a tremendous effort overnight! Here is what I can tell you from what we have seen so far: 1. Prefer horizontal orientation of card rather than vertical. 2. Prefer the white cards with the blue and gray logo vs. the darker colors 3. Would like the back of the card to be white with room for a hand written note 4. Clear plastic cards are not a hit 5. Not a fan of card that look like the data is presented on any kind of a 'tab' or website type icons. Thanks for the many creative ideas, we are excited about this contest. mt

```html
<!DOCTYPE html>
<html lang="en">
<head>
<meta charset="utf-8">
<title>Blue Pine Lodge – Business Card</title>
<link rel="stylesheet" href="https://fonts.googleapis.com/css2?family=Questrial&display=swap">
<style>
  :root{
    --stage:#e6e7ea;
    --navy:#1b2a8c;
    --navy-deep:#141f6e;
    --grey-band:#a9adb5;
    --white:#ffffff;
    --ink:#1f2a5c;
  }
  *{margin:0;padding:0;box-sizing:border-box}
  html,body{width:1200px;height:897px;overflow:hidden}
  body{
    background:var(--stage);
    font-family:"Questrial",sans-serif;
    display:flex;flex-direction:column;align-items:center;justify-content:center;gap:40px;
  }
  .card{
    width:640px;height:366px;position:relative;overflow:hidden;
    box-shadow:0 6px 18px rgba(0,0,0,.18);
  }
  .wordmark{display:flex;align-items:center;gap:10px;color:var(--ink);white-space:nowrap}
  .wordmark-dot{width:18px;height:18px;border-radius:50%;background:var(--ink);flex:none}

  /* back: white, logo near the top, open space below for a handwritten note */
  .card-back{background:var(--white)}
  .card-back .wordmark{position:absolute;left:50%;top:44px;transform:translateX(-50%);font-size:28px}

  /* front */
  .card-front{background:var(--navy)}
  .card-front svg.shape{position:absolute;inset:0}
  .card-front .wordmark{position:absolute;left:36px;top:108px;font-size:30px}
  .details{
    position:absolute;right:26px;top:40px;width:220px;text-align:right;color:var(--white);
  }
  .name{font-size:17px;letter-spacing:1px;text-transform:uppercase}
  .title{font-size:10px;letter-spacing:1.5px;text-transform:uppercase;margin-top:2px}
  .address{font-size:11px;line-height:1.45;margin-top:28px}
  .contacts{list-style:none;margin-top:34px;font-size:10.5px}
  .contacts li{display:flex;justify-content:flex-end;align-items:center;gap:8px;height:19px}
  .contacts svg{width:11px;height:11px;fill:var(--white);flex:none}
</style>
</head>
<body>
  <section class="card card-back" aria-label="Card back">
    <div class="wordmark"><span class="wordmark-dot"></span><span>bluepinelodge.net</span></div>
  </section>

  <section class="card card-front" aria-label="Card front">
    <svg class="shape" viewBox="0 0 640 366" preserveAspectRatio="none">
      <defs>
        <linearGradient id="navyShade" x1="0" y1="0" x2="1" y2="1">
          <stop offset="0" stop-color="#1b2a8c"/>
          <stop offset="1" stop-color="#141f6e"/>
        </linearGradient>
      </defs>
      <path d="M0,0 H418 Q400,250 0,302 Z" fill="var(--grey-band)"/>
      <path d="M0,0 H404 Q386,238 0,288 Z" fill="var(--white)"/>
      <path d="M0,302 Q400,250 418,0 H640 V366 H0 Z" fill="url(#navyShade)" opacity=".35"/>
    </svg>

    <div class="wordmark"><span class="wordmark-dot"></span><span>bluepinelodge.net</span></div>

    <div class="details">
      <p class="name">Morris Trulsow</p>
      <p class="title">President</p>
      <p class="address">418 Dunmere Lane Suite 207<br>Spring, TX 77291</p>
      <ul class="contacts">
        <li>012 555 0147<svg viewBox="0 0 12 12"><path d="M2 1h3l1 3-1.5 1a7 7 0 0 0 2.5 2.5L8 6l3 1v3a1 1 0 0 1-1 1A9 9 0 0 1 1 2a1 1 0 0 1 1-1z"/></svg></li>
        <li>012 555 0148<svg viewBox="0 0 12 12"><rect x="3" y="0.5" width="6" height="11" rx="1"/></svg></li>
        <li>012 555 0149<svg viewBox="0 0 12 12"><rect x="3" y="1" width="6" height="3"/><rect x="1" y="4.5" width="10" height="5" rx="1"/><rect x="3" y="8" width="6" height="3"/></svg></li>
        <li>morris@bluepinelodge.net<svg viewBox="0 0 12 12"><path d="M1 2.5h10v7H1z M1 2.5l5 4 5-4" fill="none" stroke="#fff" stroke-width="1.2"/></svg></li>
        <li>www.bluepinelodge.net<svg viewBox="0 0 12 12"><circle cx="6" cy="6" r="5" fill="none" stroke="#fff" stroke-width="1.2"/><path d="M1 6h10M6 1c-3 3-3 7 0 10M6 1c3 3 3 7 0 10" fill="none" stroke="#fff" stroke-width="1"/></svg></li>
      </ul>
    </div>
  </section>
</body>
</html>
```